Letter and Services

Our current letter is two sided, one tells about our company, and the other lists our services in the same categories as found on our website. We like light and bright marketing and are looking from a change over our old materials. Whites, the teal in our logo, greys, etc. modern, clean, upscale feeling. We can provide updated text for the letter to go with the marketing materials.

```html
<!DOCTYPE html>
<html lang="en">
<head>
<meta charset="utf-8">
<title>Willow Crest Properties – Services</title>
<link href="https://fonts.googleapis.com/css2?family=Inter:wght@400;700&display=swap" rel="stylesheet">
<style>
  :root {
    --teal: #0d6e6d;
    --ink: #2b2b2b;
    --paper: #ffffff;
  }
  * { box-sizing: border-box; margin: 0; padding: 0; }
  html, body { width: 927px; height: 1200px; overflow: hidden; background: var(--paper); }
  body { position: relative; font-family: "Inter", "Helvetica Neue", Arial, sans-serif; color: var(--ink); }

  .service-card {
    position: absolute;
    width: 348px;
    height: 348px;
    border: 5.5px solid var(--teal);
    background: var(--paper);
  }
  .service-card::before {
    content: "";
    position: absolute;
    inset: 5px;
    border: 1px solid var(--teal);
  }
  .col-left  { left: 93px; }
  .col-right { left: 479px; }
  .row-1 { top: 40px; }
  .row-2 { top: 421px; }
  .row-3 { top: 802px; }

  .brand-mark {
    position: absolute;
    top: 37px;
    left: 0; right: 0;
    display: flex;
    justify-content: center;
    align-items: center;
    gap: 6px;
    font-size: 12.5px;
    font-weight: 400;
    color: var(--ink);
    letter-spacing: 0.02em;
  }
  .brand-mark .brand-square {
    width: 9px; height: 9px;
    background: var(--teal);
  }

  .service-title {
    position: absolute;
    top: 94px;
    left: 0; right: 0;
    text-align: center;
    font-size: 18.5px;
    font-weight: 700;
    color: var(--teal);
    line-height: 1.3;
  }
  .service-title.is-raised { top: 91px; }

  .service-list {
    position: absolute;
    top: 132px;
    left: 56px;
    right: 30px;
    list-style: none;
    font-size: 13px;
    line-height: 16.3px;
  }
  .service-list.is-tight { top: 129px; }
  .service-list li {
    position: relative;
    margin-bottom: 12.6px;
  }
  .service-list.is-tight li { margin-bottom: 8.5px; }
  .service-list li::before {
    content: "•";
    position: absolute;
    left: -19px;
    font-size: 9px;
  }
</style>
</head>
<body>

<section class="service-card col-left row-1">
  <div class="brand-mark"><span class="brand-square"></span>Willow Crest Properties</div>
  <h2 class="service-title">Investment Property Selection</h2>
  <ul class="service-list">
    <li>Analyze current or prospective investment properties to determine prospective return on investment.</li>
    <li>Recommend rental rates and/or improvements to increase profitability.</li>
    <li>Assist in the search and purchase of properties to grow your portfolio.</li>
  </ul>
</section>

<section class="service-card col-right row-1">
  <div class="brand-mark"><span class="brand-square"></span>Willow Crest Properties</div>
  <h2 class="service-title">Tenant Procurement</h2>
  <ul class="service-list">
    <li>A broad scope of advertising to lease your property quickly.</li>
    <li>Tenant screening with comprehensive background check, employment verification, landlord verification, and reference check.</li>
    <li>In person as well as online applications and lease signing available to secure a lease for your property quickly.</li>
  </ul>
</section>

<section class="service-card col-left row-2">
  <div class="brand-mark"><span class="brand-square"></span>Willow Crest Properties</div>
  <h2 class="service-title is-raised">Lease Administration</h2>
  <ul class="service-list is-tight">
    <li>Move-in inspection and quarterly property inspections.</li>
    <li>Rent collection with online payment and automatic debit options for tenants.</li>
    <li>Payment of property invoices</li>
    <li>Active resident retention and lease renewals.</li>
    <li>Addressing lease violations and working with our attorney or yours for legal action when necessary.</li>
  </ul>
</section>

<section class="service-card col-right row-2">
  <div class="brand-mark"><span class="brand-square"></span>Willow Crest Properties</div>
  <h2 class="service-title">Repairs and Maintenance</h2>
  <ul class="service-list">
    <li>Coordination of standard repairs and tenant work orders.</li>
    <li>Implementation of capital improvement and preventive maintenance plan.</li>
    <li>Vendor negotiations and management.</li>
    <li>24/7 Emergency maintenance.</li>
  </ul>
</section>

<section class="service-card col-left row-3">
  <div class="brand-mark"><span class="brand-square"></span>Willow Crest Properties</div>
  <h2 class="service-title">Move Out &amp; Turnover</h2>
  <ul class="service-list">
    <li>Move out property inspection with tenant.</li>
    <li>Security Deposits charges, refunds, and accounting, in accordance with PA state law.</li>
    <li>If applicable, aggressive collection of any charges above security deposit.</li>
    <li>Arrangement and management of vendors to prepare the property for the new tenant.</li>
  </ul>
</section>

<section class="service-card col-right row-3">
  <div class="brand-mark"><span class="brand-square"></span>Willow Crest Properties</div>
  <h2 class="service-title">Additional Owner Benefits</h2>
  <ul class="service-list">
    <li>Customized owner portal with easy access to real time reports.</li>
    <li>Monthly property overview report mailed.</li>
    <li>Annual property report with recommended revenue increases.</li>
    <li>Five year capital plan with suggested improvements.</li>
    <li>End of the year tax reforms.</li>
  </ul>
</section>

</body>
</html>
```